cover for CD- Single.

This design is for a CD cover. The design is at your disposal, using all of your creative talents.
Things to improve the photo: Cleaning the face, removing blemishes.
Design in black and white would be an option (Color would be another option). I reiterate it is up to your taste and criteria, any reform and art on the cover of Cd.
Name of the single: El Camino del Alba Serena
Artist Name: Marisol Quenteva

Target Market(s)

Single Music

Industry/Entity Type

Music

Colors

Designer to choose colors to be used in the design.

Requirements
Must have
• style, elegance, professionalism, spontaneity
Nice to have
• I want it to be as professional as possible.
Should not have
• Spelling errors.

```html
<!DOCTYPE html>
<html lang="es">
<head>
<meta charset="utf-8">
<title>El Camino del Alba Serena — Marisol Quenteva</title>
<link rel="stylesheet" href="https://fonts.googleapis.com/css2?family=Federo&family=Tenor+Sans&display=swap">
<style>
  :root {
    --page-bg: #a2bfd3;
    --sleeve-light: #e9e6ec;
    --sleeve-mid: #d3cfd8;
    --sleeve-shade: #bdb8c3;
    --paint-blue: #5f97c0;
    --paint-blue-soft: #b3cfe0;
    --photo-grey: #b9b9bc;
    --photo-pale: #d8d2d0;
    --photo-skin: #e7bcaa;
    --photo-skin-deep: #d39d89;
    --photo-hair: #223f69;
    --photo-hair-deep: #17305a;
    --chrome-white: #ffffff;
    --chrome-light: #f1f1f4;
    --chrome-mid: #b9b9c3;
    --chrome-dark: #5d5d68;
    --ink: #151515;
  }
  * { margin: 0; padding: 0; box-sizing: border-box; }
  html, body {
    width: 1200px; height: 848px; overflow: hidden;
    background: var(--page-bg);
  }
  .cover {
    position: absolute;
    left: 240px; top: 64px;
    width: 720px; height: 720px;
    overflow: hidden;
    background:
      radial-gradient(ellipse 45% 14% at 30% 4%, var(--sleeve-shade) 0%, transparent 70%),
      radial-gradient(ellipse 30% 45% at 96% 45%, var(--sleeve-shade) 0%, transparent 70%),
      linear-gradient(165deg, var(--sleeve-light) 0%, var(--sleeve-mid) 50%, var(--sleeve-light) 100%);
  }
  .cover__texture {
    position: absolute; inset: 0;
    width: 100%; height: 100%;
    opacity: .35;
    mix-blend-mode: multiply;
  }
  .cover__paint {
    position: absolute;
    left: -20px; top: 350px;
    width: 120px; height: 330px;
    background: linear-gradient(180deg, transparent 0%, var(--paint-blue-soft) 20%, var(--paint-blue) 55%, var(--paint-blue-soft) 85%, transparent 100%);
    filter: blur(5px);
    opacity: .8;
  }
  .cover__paint--bottom {
    left: 40px; top: 668px;
    width: 640px; height: 60px;
    background: linear-gradient(90deg, var(--paint-blue) 0%, var(--paint-blue-soft) 50%, transparent 100%);
    opacity: .6;
  }
  .cover__photo {
    position: absolute;
    left: 57px; top: 59px;
    width: 607px; height: 603px;
    background:
      linear-gradient(115deg,
        var(--photo-grey) 0%,
        var(--photo-pale) 20%,
        var(--photo-skin) 38%,
        var(--photo-skin-deep) 55%,
        var(--photo-skin) 64%,
        var(--photo-hair) 76%,
        var(--photo-hair-deep) 100%);
  }
  .cover__title {
    position: absolute;
    left: 0; top: 8px;
    width: 720px;
    font-family: "Federo", serif;
    font-weight: 400;
    line-height: 1;
    background: linear-gradient(180deg,
      var(--chrome-white) 0%,
      var(--chrome-light) 28%,
      var(--chrome-mid) 46%,
      var(--chrome-white) 58%,
      var(--chrome-mid) 80%,
      var(--chrome-light) 100%);
    -webkit-background-clip: text;
    background-clip: text;
    -webkit-text-fill-color: transparent;
    filter:
      drop-shadow(1px 1px 0 var(--chrome-dark))
      drop-shadow(-1px -1px 0 var(--chrome-white))
      drop-shadow(0 4px 5px rgba(40, 40, 55, .5));
  }
  .cover__title-line { display: block; white-space: nowrap; }
  .cover__title-line--first {
    font-size: 104px;
    text-align: right;
    padding-right: 26px;
  }
  .cover__title-line--second {
    font-size: 78px;
    padding-left: 28px;
    margin-top: 4px;
  }
  .cover__artist {
    position: absolute;
    left: 116px; top: 322px;
    transform-origin: left top;
    transform: rotate(90deg);
    font-family: "Tenor Sans", sans-serif;
    font-size: 34px;
    line-height: 1;
    color: var(--ink);
    white-space: nowrap;
  }
</style>
</head>
<body>
  <main class="cover">
    <svg class="cover__texture" aria-hidden="true">
      <filter id="paper-grain">
        <feTurbulence type="fractalNoise" baseFrequency="0.9" numOctaves="2" seed="4"/>
        <feColorMatrix type="saturate" values="0"/>
      </filter>
      <rect width="100%" height="100%" filter="url(#paper-grain)"/>
    </svg>
    <div class="cover__paint"></div>
    <div class="cover__paint cover__paint--bottom"></div>
    <div class="cover__photo" role="img" aria-label="Portrait photo of the singer with eyes closed, hand resting near her ear"></div>
    <h1 class="cover__title">
      <span class="cover__title-line cover__title-line--first">El Camino</span>
      <span class="cover__title-line cover__title-line--second">del Alba Serena</span>
    </h1>
    <p class="cover__artist">Marisol Quenteva</p>
  </main>
</body>
</html>
```